"Cork Hollow Excursions" is a top notch Santa Barbara County Wine Tour company.

We provide scenic, boutique and custom wine tours. I need the card to be clean and classy. I will provide our logo. I would like the logo to cover the back side of the card as an option and would like to see a couple color options other then our signature green and gold. I would like to see some creative options and let the designers come up with options.
I need cards for myself and my team. The final design should communicate "An authentic and boutique wine tour experience"
Please use my website for reference www.corkhollowexcursions.com

Target Market(s)

We have a wide range of clients from millennials to baby boomers

Industry/Entity Type

Tour

Contact Information for Business Card

Contact info:
Dale Munford
805-291-6384
info@corkhollowexcursions.com
corkhollowexcursions.com

Colors

Designer to choose colors to be used in the design.

Requirements
Must have
• my logo
Nice to have
• *I would like to have the backside side with the logo and the company statement
• "An authentic and boutique wine tour experience" as an option.
• *I would also like to see what the designers can create!
• *I would like to see an option that incorporates or social: snapgrid, rovia, route scout
Should not have
• I do not want it too busy.

```html
<!DOCTYPE html>
<html lang="en">
<head>
<meta charset="utf-8">
<title>Cork Hollow Excursions — Business Card</title>
<link rel="stylesheet" href="https://fonts.googleapis.com/css2?family=Roboto:wght@400;500;700&display=swap">
<style>
  :root {
    --backdrop: #363435;
    --card: #ffffff;
    --ink: #333333;
    --gold: #a08a6a;
    --vine-green: #3d7a4c;
  }
  html, body {
    margin: 0;
    padding: 0;
    width: 1200px;
    height: 1000px;
    overflow: hidden;
    background: var(--backdrop);
    font-family: "Roboto", Arial, sans-serif;
  }
  .stage {
    position: relative;
    width: 1200px;
    height: 1000px;
  }
  .card {
    position: absolute;
    left: 322px;
    width: 556px;
    height: 317px;
    background: var(--card);
    border-radius: 14px;
  }
  .card--front { top: 165px; }
  .card--back  { top: 519px; }

  .brand-name {
    margin: 0;
    color: var(--gold);
    font-weight: 500;
    letter-spacing: 0.06em;
    text-transform: uppercase;
    white-space: nowrap;
  }
  .card--front .brand-name {
    position: absolute;
    left: 46px;
    top: 42px;
    font-size: 25px;
  }
  .card--back .brand {
    position: absolute;
    inset: 0;
    display: flex;
    align-items: center;
    justify-content: center;
    gap: 12px;
  }
  .brand-mark {
    width: 14px;
    height: 14px;
    border-radius: 50%;
    background: var(--vine-green);
  }
  .card--back .brand-name { font-size: 24px; }

  .contact-block {
    position: absolute;
    left: 31px;
    top: 194px;
  }
  .person-name {
    margin: 0 0 11px;
    font-size: 17px;
    font-weight: 700;
    color: var(--ink);
  }
  .contact-list {
    list-style: none;
    margin: 0;
    padding: 0;
  }
  .contact-list li {
    display: flex;
    align-items: center;
    gap: 7px;
    height: 20px;
    font-size: 15px;
    color: var(--ink);
  }
  .contact-icon {
    width: 12px;
    height: 12px;
    flex: none;
  }
</style>
</head>
<body>
<main class="stage">
  <section class="card card--front">
    <p class="brand-name">Cork Hollow Excursions</p>

    <div class="contact-block">
      <p class="person-name">Dale Munford</p>
      <ul class="contact-list">
        <li>
          <svg class="contact-icon" viewBox="0 0 12 12" aria-hidden="true">
            <path d="M3 1.5 L4.6 3.8 L3.6 5 Q4.7 7.3 7 8.4 L8.2 7.4 L10.5 9 L9.4 10.6 Q4.8 10.4 1.4 2.6 Z" fill="none" stroke="var(--vine-green)" stroke-width="1"/>
          </svg>
          805-291-6384
        </li>
        <li>
          <svg class="contact-icon" viewBox="0 0 12 12" aria-hidden="true">
            <rect x="1" y="3" width="10" height="7" fill="var(--vine-green)"/>
            <path d="M1 3 L6 7 L11 3" fill="none" stroke="#fff" stroke-width="1"/>
          </svg>
          info@corkhollowexcursions.com
        </li>
        <li>
          <svg class="contact-icon" viewBox="0 0 12 12" aria-hidden="true">
            <g fill="none" stroke="var(--vine-green)" stroke-width="0.9">
              <circle cx="6" cy="6" r="5"/>
              <ellipse cx="6" cy="6" rx="2.2" ry="5"/>
              <path d="M1 6 H11 M2 3.5 H10 M2 8.5 H10"/>
            </g>
          </svg>
          corkhollowexcursions.com
        </li>
      </ul>
    </div>
  </section>

  <section class="card card--back">
    <div class="brand">
      <span class="brand-mark" aria-hidden="true"></span>
      <p class="brand-name">Cork Hollow Excursions</p>
    </div>
  </section>
</main>
</body>
</html>
```